Teilnehmerzertifikat für Expeditionsmobil
Zielgruppe
Wir bitten alles Rund um das Thema Expeditionsmobil an. Unter anderem unsere Lagerfeuer und Weite Fahrt nach Tunesien und dafür benötige ich ein Teilnehmer Zertifikat.
Aufgabenstellung
Im Hintergrund soll ein Bild von der Sahara verarbeitet sein und im Vordergrund möchte ich von jedem Teilnehmer ein Bild mit dem eigenen Expeditonsfahrzeug einfügen. Das Zertifikat soll persöhnlich und wie von einem Freund sein

```html
<!DOCTYPE html>
<html lang="de">
<head>
<meta charset="utf-8">
<title>Teilnehmer-Zertifikat – Lagerfeuer und Weite Fahrt</title>
<link rel="stylesheet" href="https://fonts.googleapis.com/css2?family=Rubik+Dirt&family=Montserrat:wght@800&family=Lexend:wght@300;400&family=Allura&display=swap">
<style>
  :root {
    --page-bg: #eeeeee;
    --ink-black: #0b0b0b;
    --signal-red: #e01f23;
    --desert-grey-light: #8a8a8a;
    --desert-grey-dark: #3c3c3c;
    --paper-white: #f4f4f4;
    --photo-sand: #b8774a;
    --photo-sky: #8e8aa0;
  }
  * { box-sizing: border-box; margin: 0; padding: 0; }
  html, body { width: 1200px; height: 800px; overflow: hidden; background: var(--page-bg); }

  .certificate {
    position: absolute; left: 30px; top: 20px;
    width: 1140px; height: 760px;
    background: var(--ink-black);
    overflow: hidden;
    box-shadow: 0 6px 24px rgba(0,0,0,.25);
    font-family: "Lexend", sans-serif;
    color: var(--paper-white);
  }
  .desert-backdrop {
    position: absolute; left: 0; top: 0; width: 100%; height: 470px;
    background: linear-gradient(180deg, var(--desert-grey-light) 0%, #6e6e6e 45%, var(--desert-grey-dark) 100%);
  }
  .shape-layer { position: absolute; inset: 0; }

  .title {
    position: absolute; left: 80px; top: 50px;
    font-family: "Rubik Dirt", sans-serif;
    font-size: 60px; line-height: 1.0; letter-spacing: 3px;
    color: var(--paper-white); text-transform: uppercase;
  }
  .awarded-to {
    position: absolute; left: 340px; top: 186px;
    font-weight: 300; font-size: 28px;
  }
  .recipient { position: absolute; left: 210px; top: 250px; }
  .recipient span {
    display: block; width: fit-content;
    font-family: "Montserrat", sans-serif; font-weight: 800;
    font-size: 42px; letter-spacing: 2px; line-height: 1;
    padding: 10px 22px; color: var(--paper-white);
  }
  .recipient .first-name { background: var(--signal-red); margin-left: 10px; }
  .recipient .last-name { background: var(--ink-black); }

  .message {
    position: absolute; left: 100px; top: 462px; width: 640px;
    font-size: 17px; line-height: 1.35; font-weight: 400;
  }
  .message p + p { margin-top: 4px; }

  .closing {
    position: absolute; left: 290px; top: 612px;
    display: flex; align-items: baseline; gap: 16px;
  }
  .closing .date { font-size: 18px; }
  .closing .signature {
    font-family: "Allura", cursive; font-size: 50px; line-height: 1;
  }

  .vehicle-photo {
    position: absolute; left: 715px; top: 165px;
    width: 390px; height: 280px;
    background: var(--paper-white); padding: 10px;
    box-shadow: 0 4px 12px rgba(0,0,0,.35);
  }
  .vehicle-photo .fill {
    width: 100%; height: 100%;
    background: linear-gradient(180deg, var(--photo-sky) 0%, var(--photo-sand) 22%, #a0613a 60%, #7a4a30 100%);
  }

  .tour-name {
    position: absolute; left: 800px; top: 478px; width: 300px;
    font-family: "Montserrat", sans-serif; font-weight: 800;
    font-size: 34px; line-height: 1.05; text-transform: uppercase;
    color: var(--paper-white);
  }

  .brand {
    position: absolute; right: 70px; bottom: 34px;
    display: flex; align-items: center; gap: 12px;
    font-family: "Montserrat", sans-serif; font-weight: 800;
    font-size: 30px; color: var(--signal-red); text-transform: uppercase;
  }
  .brand .dot { width: 34px; height: 34px; border-radius: 50%; background: var(--signal-red); }
</style>
</head>
<body>
  <main class="certificate">
    <div class="desert-backdrop" role="img" aria-label="Sahara-Landschaft in Graustufen als Hintergrund"></div>

    <svg class="shape-layer" viewBox="0 0 1140 760" aria-hidden="true">
      <polygon fill="var(--ink-black)" points="0,0 640,0 636,40 660,80 640,120 668,170 644,210 660,250 620,262 560,256 480,268 400,258 300,266 200,255 100,262 0,256"/>
      <polygon fill="var(--signal-red)" points="0,330 60,322 140,330 240,318 330,326 420,316 520,324 640,318 760,326 860,318 960,326 1060,316 1140,322 1140,660 1080,666 1000,658 920,668 820,660 720,670 620,660 520,670 420,662 320,672 220,664 120,674 40,666 0,670"/>
    </svg>

    <h1 class="title">Teilnehmer-<br>Zertifikat</h1>
    <p class="awarded-to">verliehen an:</p>

    <div class="recipient">
      <span class="first-name">MAXIMILLIAN</span>
      <span class="last-name">MUSTERMANN</span>
    </div>

    <figure class="vehicle-photo">
      <div class="fill" role="img" aria-label="Foto des Teilnehmers mit seinem roten Expeditionsmobil, das durch eine überflutete Wüstenpiste fährt"></div>
    </figure>

    <div class="message">
      <p>Ihr habt mit Begeisterung und Abenteuerlust an unserer gemeinsamen Reise durch Tunesien teilgenommen.</p>
      <p>Mit eurem Expeditionsmobil habt ihr die Wüste bezwungen, neue Freundschaften geschlossen und die Magie dieses einzigartigen Landes erlebt.</p>
      <p>Danke, dass ihr Teil dieser besonderen Tour wart – auf viele weitere Abenteuer!</p>
    </div>

    <div class="closing">
      <span class="date">Tunisien, 21 November 2024</span>
      <span class="signature">Jan &amp; Malte</span>
    </div>

    <p class="tour-name">Lagerfeuer und Weite Fahrt</p>

    <div class="brand">
      <span class="dot"></span>
      <span>Kranichpfad Reisen</span>
    </div>
  </main>
</body>
</html>
```